Infographic of the benefits of varying cannabinoids. Should be in SVG format with clickable links.

Our company sells cannabinoid products online, primarily tinctures of various CBD derivative blends. We need an infographic built which we will use on a landing page. I have attached a copy of our draft logo which should be incorporated into the infographic, but feel free to take some creative liberty with what I've provided.. The color scheme on the design should be appropriate for an earthy / planty product. Probably greens and light brown.

I have a list of desired effects and the different cannabinoids which will trigger said effect. The infographic should have a flow feel to it where readers will scroll through desired effects to see the cannabinoid which produces / impacts it.

The image needs to be in SVG format so that it loads quickly, can be SEO optimized, and have clickable segments built into the image. The clickable pieces of the image should in some way have a visual queue that will guide people to click or tap to open the link (which we will generally be linking to a product).

Each desired effect (pain management, insomnia, etc), and each cannabinoid, needs to be clickable within the SVG using markup.

For example,
- Anxiety - link which we will swap out for CBD/CBG product on our site
--- CBD - link which we will swap out for CBD product link on our site
--- CBG - link which we will swap out for CBG product link on our site

Here is the full list of groupings, symptoms, and mapped cannabinoids that need to be built into the infographic. Where links are present to BMS.gov, there should be a visual queue that there is a backing study from the Bureau for Medical Studies (BMS) which is a clickable link to the BMS study referenced.

- COVID Symptoms & Prevention
https://papers.medvault-index.org/35007072/
-- CBGA
-- CBDA
- Pain
https://www.medvault-index.org/lib/entries/MV2503660/ (pain management)
https://www.medvault-index.org/lib/entries/MV2828614/ (chronic pain dosage)
-- Cramps / Migraine / Headache / Phantom Limb / Spinal Injury
--- CBD
--- THC
Fibromyalgia
--- CBD
--- CBN
--- THC
-- General Pain
--- CBC
--- CBD
--- CBN
--- THC
--- THCv
-- Arthritis / Inflammation
https://www.medvault-index.org/papers/28885454 (arthritis)
https://www.medvault-index.org/lib/entries/MV2828614/ (inflammation)
--- CBC
--- CBD
--- CBDa
--- CBG
--- CBN
--- THC
--- THCa
- Sleep
-- Insomnia
https://www.medvault-index.org/lib/entries/MV5101100/
--- CBC
--- CBD
--- CBN
--- THC
- Gastro
-- General Gastro / Nausea
https://www.medvault-index.org/volumes/VL425767/
--- CBD
--- THC
Crohn’s
https://www.medvault-index.org/lib/entries/MV2748879/
--- CBD
--- THC
--- THCa
- Mood
-- Anxiety
https://www.medvault-index.org/lib/entries/MV4604171/
--- CBD
--- CBG
-- ADHD / Stress
https://www.medvault-index.org/papers/28576350
--- CBD
--- THC
--- PTSD
--- CBD
--- CBG
--- THC
-- Depression
https://papers.medvault-index.org/24923339/
--- CBC
--- CBD
--- CBG
--- CBN
--- THC
- Neuro
-- Epilepsy / Seizures
https://www.medvault-index.org/papers/26800377
--- CBD
--- CBN
--- THCa
--- THCv
-- Multiple Sclerosis
https://www.medvault-index.org/lib/entries/MV5874292/
--- CBD
--- CBN
--- THC
--- THCa
-- Alzheimer’s
https://www.medvault-index.org/papers/28217094
--- CBC
--- CBD
--- CBG
--- THC
--- THCa

Target Market(s)

CBD users who are looking for different cannabinoids based on health benefits.

Industry/Entity Type

Cannabis / Hemp

Requirements
Must have
• SVG format with clickable links on the different benefits and on each cannabinoid.

```html
<!DOCTYPE html>
<html lang="en">
<head>
<meta charset="utf-8">
<title>Verdalis – Cannabinoids by Desired Effect</title>
<link rel="stylesheet" href="https://fonts.googleapis.com/css2?family=Exo+2:wght@500;600;700&display=swap">
<style>
  :root {
    --leaf: #4e7a3a;
    --leaf-dark: #3d6230;
    --bark: #8a6a47;
    --ink: #2a2418;
    --paper: #fbf8f2;
    --pill-start: #ece3d3;
    --pill-end: #fffdf9;
    --pill-shadow: rgba(70, 50, 20, 0.18);
  }
  * { box-sizing: border-box; margin: 0; padding: 0; }
  html, body { width: 690px; height: 1200px; overflow: hidden; background: var(--paper); }
  body { font-family: "Exo 2", sans-serif; color: var(--ink); }

  .poster {
    position: relative;
    width: 690px;
    height: 1200px;
    border: 6px solid var(--bark);
    background: var(--paper);
  }

  .brand {
    position: absolute;
    top: 60px;
    left: 0;
    width: 100%;
    text-align: center;
    font-size: 42px;
    font-weight: 600;
    letter-spacing: 1px;
    color: var(--ink);
    line-height: 1;
  }

  .group-badge {
    position: absolute;
    left: 30px;
    width: 50px;
    height: 50px;
    border-radius: 50%;
    background: var(--leaf);
    box-shadow: 0 3px 6px var(--pill-shadow);
    z-index: 2;
  }

  .group-title {
    position: absolute;
    left: 52px;
    height: 30px;
    padding: 0 14px 0 36px;
    border-radius: 0 15px 15px 0;
    background: linear-gradient(90deg, var(--pill-start), var(--pill-end));
    box-shadow: 2px 3px 5px var(--pill-shadow);
    display: flex;
    align-items: center;
    font-size: 19px;
    font-weight: 600;
    font-variant: small-caps;
    color: var(--ink);
    text-decoration: none;
    z-index: 1;
    white-space: nowrap;
  }

  .covid-line {
    position: absolute;
    left: 52px;
    display: flex;
    align-items: center;
    z-index: 1;
  }
  .covid-line .group-title { position: relative; left: 0; z-index: 2; }
  .covid-tags {
    height: 28px;
    margin-left: -6px;
    padding: 0 12px 0 14px;
    border-radius: 0 14px 14px 0;
    background: var(--pill-end);
    box-shadow: 2px 3px 5px var(--pill-shadow);
    display: flex;
    align-items: center;
  }

  .effect-row {
    position: absolute;
    left: 150px;
    height: 28px;
    padding-right: 12px;
    border-radius: 14px;
    background: linear-gradient(90deg, var(--pill-start), var(--pill-end) 45%);
    box-shadow: 2px 3px 5px var(--pill-shadow);
    display: flex;
    align-items: center;
  }
  .effect-row.tall { height: 32px; }

  .effect-name {
    flex: 0 0 155px;
    padding-left: 14px;
    font-size: 10.5px;
    font-weight: 500;
    line-height: 1.1;
    white-space: nowrap;
    color: var(--ink);
    text-decoration: none;
  }

  .compounds { display: flex; gap: 11px; }

  .compound {
    width: 46px;
    height: 15px;
    border-radius: 8px;
    background: var(--leaf);
    color: #fff;
    font-size: 10px;
    font-weight: 500;
    display: flex;
    align-items: center;
    justify-content: center;
    text-decoration: none;
    box-shadow: 0 1px 2px rgba(0,0,0,0.2);
  }
</style>
</head>
<body>
<main class="poster">

  <div class="brand">VERDALIS</div>

  <!-- COVID -->
  <div class="group-badge" role="img" aria-label="Virus icon" style="top:197px"></div>
  <div class="covid-line" style="top:207px">
    <a class="group-title" href="#covid">COVID Symptoms &amp; Prevention</a>
    <div class="covid-tags">
      <div class="compounds">
        <a class="compound" href="#cbda">CBDA</a>
        <a class="compound" href="#cbga">CBGA</a>
      </div>
    </div>
  </div>

  <!-- Pain -->
  <div class="group-badge" role="img" aria-label="Person with headache icon" style="top:305px"></div>
  <a class="group-title" href="#pain" style="top:315px">Pain</a>
  <div class="effect-row tall" style="top:315px">
    <a class="effect-name" href="#cramps">Cramps / Migraine / Headache<br>Phantom Limb / Spinal Injury</a>
    <div class="compounds"><a class="compound" href="#cbd">CBD</a><a class="compound" href="#thc">THC</a></div>
  </div>
  <div class="effect-row" style="top:356px">
    <a class="effect-name" href="#fibromyalgia">Fibromyalgia</a>
    <div class="compounds"><a class="compound" href="#cbd">CBD</a><a class="compound" href="#cbn">CBN</a><a class="compound" href="#thc">THC</a></div>
  </div>
  <div class="effect-row" style="top:396px">
    <a class="effect-name" href="#general-pain">General Pain</a>
    <div class="compounds"><a class="compound" href="#cbc">CBC</a><a class="compound" href="#cbd">CBD</a><a class="compound" href="#cbn">CBN</a></div>
  </div>
  <div class="effect-row" style="top:435px">
    <a class="effect-name" href="#arthritis">Arthritis / Inflammation</a>
    <div class="compounds"><a class="compound" href="#cbc">CBC</a><a class="compound" href="#cbd">CBD</a><a class="compound" href="#cbda">CBDa</a><a class="compound" href="#cbg">CBG</a><a class="compound" href="#cbn">CBN</a><a class="compound" href="#thc">THC</a></div>
  </div>

  <!-- Sleep -->
  <div class="group-badge" role="img" aria-label="Sleeping person icon" style="top:523px"></div>
  <a class="group-title" href="#sleep" style="top:533px">Sleep</a>
  <div class="effect-row" style="top:534px">
    <a class="effect-name" href="#insomnia">Insomnia</a>
    <div class="compounds"><a class="compound" href="#cbd">CBD</a><a class="compound" href="#cbd">CBD</a><a class="compound" href="#cbn">CBN</a><a class="compound" href="#thc">THC</a></div>
  </div>

  <!-- Gastro -->
  <div class="group-badge" role="img" aria-label="Digestive system icon" style="top:640px"></div>
  <a class="group-title" href="#gastro" style="top:650px">Gastro</a>
  <div class="effect-row" style="top:651px">
    <a class="effect-name" href="#nausea">General Gastro / Nausea</a>
    <div class="compounds"><a class="compound" href="#cbd">CBD</a><a class="compound" href="#thc">THC</a></div>
  </div>
  <div class="effect-row" style="top:690px">
    <a class="effect-name" href="#crohns">Crohn’s</a>
    <div class="compounds"><a class="compound" href="#cbd">CBD</a><a class="compound" href="#thc">THC</a><a class="compound" href="#thca">THCa</a></div>
  </div>

  <!-- Mood -->
  <div class="group-badge" role="img" aria-label="Mood faces icon" style="top:769px"></div>
  <a class="group-title" href="#mood" style="top:779px">Mood</a>
  <div class="effect-row" style="top:780px">
    <a class="effect-name" href="#anxiety">Anxiety</a>
    <div class="compounds"><a class="compound" href="#cbd">CBD</a><a class="compound" href="#cbg">CBG</a></div>
  </div>
  <div class="effect-row" style="top:820px">
    <a class="effect-name" href="#adhd">ADHD / Stress</a>
    <div class="compounds"><a class="compound" href="#cbd">CBD</a><a class="compound" href="#thc">THC</a></div>
  </div>
  <div class="effect-row" style="top:860px">
    <a class="effect-name" href="#ptsd">PTSD</a>
    <div class="compounds"><a class="compound" href="#cbd">CBD</a><a class="compound" href="#cbg">CBG</a><a class="compound" href="#thc">THC</a></div>
  </div>
  <div class="effect-row" style="top:901px">
    <a class="effect-name" href="#depression">Depression</a>
    <div class="compounds"><a class="compound" href="#cbc">CBC</a><a class="compound" href="#cbd">CBD</a><a class="compound" href="#cbg">CBG</a><a class="compound" href="#cbn">CBN</a><a class="compound" href="#thc">THC</a></div>
  </div>

  <!-- Neuro -->
  <div class="group-badge" role="img" aria-label="Brain icon" style="top:986px"></div>
  <a class="group-title" href="#neuro" style="top:996px">Neuro</a>
  <div class="effect-row" style="top:997px">
    <a class="effect-name" href="#epilepsy">Epilepsy / Seizures</a>
    <div class="compounds"><a class="compound" href="#cbd">CBD</a><a class="compound" href="#cbn">CBN</a><a class="compound" href="#thca">THCa</a><a class="compound" href="#thcv">THCv</a></div>
  </div>
  <div class="effect-row" style="top:1037px">
    <a class="effect-name" href="#ms">Multiple Sclerosis</a>
    <div class="compounds"><a class="compound" href="#cbd">CBD</a><a class="compound" href="#cbn">CBN</a><a class="compound" href="#thc">THC</a><a class="compound" href="#thca">THCa</a></div>
  </div>
  <div class="effect-row" style="top:1078px">
    <a class="effect-name" href="#alzheimers">Alzheimer’s</a>
    <div class="compounds"><a class="compound" href="#cbc">CBC</a><a class="compound" href="#cbd">CBD</a><a class="compound" href="#cbg">CBG</a><a class="compound" href="#thc">THC</a><a class="compound" href="#thca">THCa</a></div>
  </div>

</main>
</body>
</html>
```